Marlowen Promotional Flier

1 page flier that can be emailed to perspective customers or printed and distributed. Flier should use logo and design cues from our website, marlowen.example. We offer equipment financing and business loans to small businesses. The design should incorporate the highlights of working with Marlowen which include:

Benefits:
- Approvals In Hours
- Automated, Easy Application Process
- New and Used Equipment Financed
- 92% Approval Rate
-Flexible Terms
- Superior Support

Program Minimums:
- 450 Minimum Credit Score
- 2 months minimum Time In Business
- $7,500/mo minimum revenue deposits

Target Market(s)

Small To Medium Sized businesses

Industry/Entity Type

Finance

Font styles to use
Sans Serif

Colors
0555a3
3075b4
85acd3
cfdeed

Requirements
Should not have
• No cheesy money bags or dollar signs fling aorund. Should be professional

```html
<!DOCTYPE html>
<html lang="en">
<head>
<meta charset="utf-8">
<title>Marlowen Business Loans Flier</title>
<link rel="stylesheet" href="https://fonts.googleapis.com/css2?family=Montserrat:wght@300;400;500;700;800;900&display=swap">
<style>
  :root {
    --blue-deep: #0555a3;
    --blue: #3075b4;
    --blue-band: #3d7bc0;
    --blue-light: #85acd3;
    --blue-pale: #cfdeed;
    --green: #7ec98e;
    --green-bullet: #6cc07a;
    --grey-text: #666666;
    --grey-band: #555557;
    --grey-stripe: #7d7f82;
    --ink: #111111;
    --paper: #ffffff;
    --backdrop: #e9ecef;
  }
  * { box-sizing: border-box; margin: 0; padding: 0; }
  html, body { width: 1200px; height: 800px; overflow: hidden; }
  body {
    background: var(--backdrop);
    font-family: "Montserrat", Arial, sans-serif;
    position: relative;
  }
  .flier {
    position: absolute;
    left: 306px;
    top: 20px;
    width: 1028px;
    height: 1330px;
    background: var(--paper);
    transform: scale(0.5714);
    transform-origin: top left;
    overflow: hidden;
    box-shadow: 0 4px 24px rgba(0,0,0,.15);
  }
  .art { position: absolute; left: 0; top: 0; }
  .brand {
    position: absolute; left: 58px; top: 50px;
    font-size: 68px; font-weight: 400; color: var(--blue);
    letter-spacing: -2px;
  }
  .headline { position: absolute; left: 64px; top: 162px; color: var(--grey-text); }
  .headline .light { display: block; font-size: 47px; font-weight: 400; letter-spacing: 1px; line-height: 56px; }
  .headline .bold { display: block; font-size: 49px; font-weight: 900; line-height: 52px; }
  .intro {
    position: absolute; left: 66px; top: 292px; width: 340px;
    font-size: 25px; font-weight: 800; line-height: 31px; color: var(--blue);
  }
  .band {
    position: absolute; left: 60px; height: 36px;
    background: var(--blue);
    clip-path: polygon(0 0, 100% 0, calc(100% - 14px) 100%, 0 100%);
    color: var(--paper); font-weight: 800; font-size: 28px;
    line-height: 38px; padding-left: 10px; letter-spacing: .5px;
  }
  .benefits-band { top: 477px; width: 198px; }
  .minimums-band { top: 726px; width: 380px; }
  .about-band { top: 886px; width: 275px; }
  .steps-band { top: 1074px; width: 327px; }
  .benefit-list {
    position: absolute; left: 64px; top: 524px; list-style: none;
    font-size: 20px; line-height: 27.6px; color: var(--ink);
  }
  .benefit-list li { position: relative; padding-left: 21px; }
  .benefit-list li::before {
    content: ""; position: absolute; left: 0; top: 8px;
    border-left: 11px solid var(--green-bullet);
    border-top: 6px solid transparent; border-bottom: 6px solid transparent;
  }
  .minimum-list {
    position: absolute; left: 72px; top: 772px; list-style: none;
    font-size: 19px; font-weight: 700; line-height: 28px; color: var(--ink);
  }
  .minimum-list li { display: flex; align-items: center; gap: 9px; }
  .minimum-list svg { flex: none; }
  .about-text {
    position: absolute; left: 74px; top: 934px; width: 750px;
    font-size: 15.2px; line-height: 18.4px; color: var(--ink);
  }
  .steps { position: absolute; left: 73px; top: 1127px; width: 920px; height: 100px; }
  .step { position: absolute; top: 0; display: flex; gap: 10px; }
  .step-icon {
    flex: none; width: 70px; height: 70px; border-radius: 50%;
    background: var(--blue); display: flex; align-items: center; justify-content: center;
  }
  .step p { font-size: 15.4px; font-weight: 700; line-height: 18.6px; color: var(--ink); }
  .step-1 { left: 0; } .step-1 p { width: 148px; }
  .step-2 { left: 241px; } .step-2 p { width: 126px; padding-top: 2px; }
  .step-3 { left: 457px; } .step-3 p { width: 116px; padding-top: 2px; }
  .step-4 { left: 674px; } .step-4 p { width: 150px; }
  .contact-bar {
    position: absolute; left: 0; top: 1250px; width: 1028px; height: 80px;
    background: var(--blue-band); color: var(--paper);
  }
  .contact-title {
    position: absolute; left: 0; top: 0; width: 133px; height: 80px;
    background: var(--grey-band); font-weight: 800; font-size: 22px;
    line-height: 25px; padding: 15px 0 0 28px;
  }
  .contact-item {
    position: absolute; top: 16px; display: flex; align-items: center; gap: 12px;
    font-size: 16px; line-height: 19.5px; white-space: nowrap;
  }
  .contact-icon {
    width: 46px; height: 46px; border-radius: 50%; background: var(--paper);
    display: flex; align-items: center; justify-content: center; flex: none;
  }
  .contact-phone { left: 155px; }
  .contact-address { left: 388px; }
  .contact-web { left: 748px; }
</style>
</head>
<body>
  <article class="flier">
    <svg class="art" width="1028" height="1330" viewBox="0 0 1028 1330">
      <defs>
        <linearGradient id="cityTone" x1="0" y1="0" x2="1" y2="1">
          <stop offset="0" stop-color="#3d7fc4"/>
          <stop offset="0.55" stop-color="#2d62a0"/>
          <stop offset="1" stop-color="#1b3f70"/>
        </linearGradient>
      </defs>
      <polygon points="483,0 797,0 642,150" fill="#000"/>
      <polygon points="510,595 555,595 960,985 915,985" fill="var(--grey-stripe)"/>
      <polygon points="1028,880 917,1005 1028,1130" fill="var(--green)"/>
      <path d="M797,0 L1028,0 L1028,985 L935,985 L405,478 Q385,458 405,438 Z" fill="url(#cityTone)" role="img" aria-label="Photo of a smiling businesswoman in a dark suit with arms crossed, in front of blue glass office towers"/>
    </svg>

    <div class="brand">Marlowen</div>

    <h1 class="headline">
      <span class="light">FAST· EASY·</span>
      <span class="bold">BUSINESS LOANS</span>
    </h1>

    <p class="intro">We offer equipment financing and business loans to small businesses.</p>

    <h2 class="band benefits-band">BENEFITS</h2>
    <ul class="benefit-list">
      <li>Approvals In Hours</li>
      <li>Automated, Easy Application Process</li>
      <li>New and Used Equipment Financed</li>
      <li>92% Approval Rate</li>
      <li>Flexible Terms</li>
      <li>Superior Support</li>
    </ul>

    <h2 class="band minimums-band">PROGRAM MINIMUMS</h2>
    <ul class="minimum-list">
      <li><svg width="20" height="20" viewBox="0 0 20 20"><circle cx="10" cy="10" r="10" fill="var(--blue)"/><path d="M5 10 L9 14 L15 6" stroke="#fff" stroke-width="2.6" fill="none"/></svg>450 Minimum Credit Score</li>
      <li><svg width="20" height="20" viewBox="0 0 20 20"><circle cx="10" cy="10" r="10" fill="var(--blue)"/><path d="M5 10 L9 14 L15 6" stroke="#fff" stroke-width="2.6" fill="none"/></svg>2 months minimum Time In Business</li>
      <li><svg width="20" height="20" viewBox="0 0 20 20"><circle cx="10" cy="10" r="10" fill="var(--blue)"/><path d="M5 10 L9 14 L15 6" stroke="#fff" stroke-width="2.6" fill="none"/></svg>$7,500/mo minimum revenue deposits</li>
    </ul>

    <h2 class="band about-band">WHO WE ARE</h2>
    <p class="about-text">Marlowen was started by a team of financing veterans who knew we could do it smarter, faster, and better. We grew tired of hearing customers’ complaints about endless phone calls from pushy sales people. We knew rates could be made more affordable. We never saw a need for tricky paperwork or hidden fees. So we set out with a simple idea: provide customers with the business financing they need, at the rates they want, with the experience they deserve. 10 years later, Marlowen has helped thousands of businesses access millions of dollars.</p>

    <h2 class="band steps-band">HOW IT WORKS</h2>
    <div class="steps">
      <div class="step step-1">
        <div class="step-icon"><svg width="40" height="40" viewBox="0 0 40 40" fill="none" stroke="#fff" stroke-width="2"><rect x="6" y="8" width="28" height="20" rx="2"/><path d="M2 32 H38"/><path d="M11 14 H22 M11 19 H22 M11 24 H18 M26 14 l2 2 3-4 M26 21 l2 2 3-4"/></svg></div>
        <p>Complete our free online application and upload or email your bank statements.</p>
      </div>
      <div class="step step-2">
        <div class="step-icon"><svg width="40" height="40" viewBox="0 0 40 40" fill="none" stroke="#fff" stroke-width="2"><circle cx="20" cy="22" r="13"/><path d="M20 14 V22 L26 25 M9 9 l5-3 M31 9 l-5-3"/></svg></div>
        <p>Give us a few short hours to dial up the best possible options for you.</p>
      </div>
      <div class="step step-3">
        <div class="step-icon"><svg width="40" height="40" viewBox="0 0 40 40" fill="none" stroke="#fff" stroke-width="2"><path d="M9 4 H27 L31 8 V36 H9 Z"/><path d="M14 12 H26 M14 17 H26 M14 22 H20 M20 30 l3 3 7-8"/></svg></div>
        <p>Select the dollar amount and term that works best for you.</p>
      </div>
      <div class="step step-4">
        <div class="step-icon"><svg width="40" height="40" viewBox="0 0 40 40" fill="none" stroke="#fff" stroke-width="2"><rect x="12" y="11" width="24" height="18" rx="2"/><circle cx="24" cy="20" r="4"/><path d="M2 14 H9 M4 20 H9 M2 26 H9"/></svg></div>
        <p>Your funds are transferred directly to your business checking account.</p>
      </div>
    </div>

    <footer class="contact-bar">
      <div class="contact-title">GET IN<br>TOUCH</div>
      <div class="contact-item contact-phone">
        <span class="contact-icon"><svg width="26" height="26" viewBox="0 0 24 24"><path d="M6.6 10.8a15 15 0 0 0 6.6 6.6l2.2-2.2a1 1 0 0 1 1-.25 11.4 11.4 0 0 0 3.6.57 1 1 0 0 1 1 1V20a1 1 0 0 1-1 1A17 17 0 0 1 3 4a1 1 0 0 1 1-1h3.5a1 1 0 0 1 1 1c0 1.250.2 2.45.57 3.57a1 1 0 0 1-.25 1z" fill="var(--green)"/></svg></span>
        <span>P: (555) 014-2290<br>F: (555) 014-7731</span>
      </div>
      <div class="contact-item contact-address">
        <span class="contact-icon"><svg width="26" height="26" viewBox="0 0 24 24"><path d="M12 2a7 7 0 0 0-7 7c0 5.2 7 13 7 13s7-7.8 7-13a7 7 0 0 0-7-7zm0 9.5A2.5 2.5 0 1 1 12 6.5a2.5 2.5 0 0 1 0 5z" fill="var(--green)"/></svg></span>
        <span>400 Harbor Row, Ste. 12<br>Fairbridge, California 90000</span>
      </div>
      <div class="contact-item contact-web">
        <span class="contact-icon"><svg width="26" height="26" viewBox="0 0 24 24" fill="none" stroke="var(--green)" stroke-width="1.8"><circle cx="12" cy="12" r="9"/><path d="M3 12 H21 M12 3 C8 7 8 17 12 21 M12 3 C16 7 16 17 12 21"/></svg></span>
        <span>info@marlowen.example<br>www.marlowen.example</span>
      </div>
    </footer>
  </article>
</body>
</html>
```